Rising Paths Web Design

I am starting a new company that will provide LIFE COACHING services - I have tried to design a website, but it's too complicated. Right now, it's just me - I'm the only person that will provide services through the website - I have used artmarket to purchase a logo (see below). I want to be able to update the website myself, but need a template - basic design. Because I am not technologically savvy enough to explain in words - I basically want to have a website that will provide basic information about my services (coaching), a page about me and my background, hopefully scheduling possibilities, and testimonials — also a page for writing/blogs. I bought a website through NetHarbor - so when I have a template, I guess I”d use that - but maybe I’ll need to work with a designer to actually get it up on the internet. I have a head shot that I’ll upload, too.
Target Market(s)
Clients from the independent (private school) world - teachers, administrators
Number of Pages Required
4 page
Look and feel
Each slider illustrates characteristics of the customer's brand and the style your logo design should communicate.

```html
<!DOCTYPE html>
<html lang="en">
<head>
<meta charset="utf-8">
<title>Rising Paths Life Coaching</title>
<link href="https://fonts.googleapis.com/css2?family=Poppins:wght@300;400;500;600;700&display=swap" rel="stylesheet">
<style>
:root{
  --teal:#0aa497;
  --teal-dark:#07897e;
  --teal-soft:#e6f6f4;
  --ink:#1c1c1c;
  --muted:#5d6464;
  --paper:#ffffff;
  --stage:#eef2f2;
  --panel:#fafafa;
}
*{box-sizing:border-box;margin:0;padding:0}
html,body{width:1152px;height:1200px;overflow:hidden}
body{background:var(--stage);font-family:'Poppins',sans-serif;color:var(--ink);position:relative}
.page{position:absolute;background:var(--paper);overflow:hidden;box-shadow:0 10px 30px rgba(0,0,0,.18)}
.page-home{left:141px;top:78px;width:390px;height:1044px}
.page-more{left:625px;top:90px;width:387px;height:1021px}
.abs{position:absolute}
.center{text-align:center}
.photo{position:absolute}

/* nav */
.nav{position:absolute;left:0;top:0;width:100%;height:33px;background:#fff}
.brand{position:absolute;left:37px;top:3px;width:32px;height:27px;display:flex;align-items:center;justify-content:center}
.brand-ring{position:absolute;inset:0;border:1px solid var(--teal);border-radius:50%}
.brand-name{font-size:3.4px;font-weight:500;color:var(--teal);letter-spacing:.1px;white-space:nowrap}
.nav-link{position:absolute;top:12px;font-size:5.8px;font-weight:500;color:var(--ink)}
.btn-outline-teal{position:absolute;border:1px solid var(--teal);color:var(--teal);font-size:4.8px;display:flex;align-items:center;justify-content:center;border-radius:2px;background:#fff}

/* hero */
.hero{position:absolute;left:0;top:33px;width:100%;height:236px;background:linear-gradient(120deg,#4d3f36 0%,#6b5546 35%,#8c6f58 55%,#3f342d 100%)}
.hero-shade{position:absolute;inset:0;background:rgba(20,15,12,.45)}
.hero-title{position:absolute;left:0;width:100%;top:40px;font-size:19.5px;font-weight:700;color:#fff;text-align:center;letter-spacing:-.2px}
.hero-title .accent{color:var(--teal)}
.hero-rule{position:absolute;left:169px;top:73px;width:52px;height:1px;background:var(--teal)}
.hero-copy{position:absolute;left:95px;width:200px;top:87px;font-size:7.8px;line-height:12.3px;color:#fff;text-align:center}
.btn-solid{position:absolute;background:var(--teal);color:#fff;font-size:6.6px;display:flex;align-items:center;justify-content:center;font-weight:500}
.btn-white{position:absolute;background:#fff;color:var(--teal);font-size:6.6px;display:flex;align-items:center;justify-content:center;font-weight:500}

/* services */
.service-card{position:absolute;background:#fff;box-shadow:0 2px 8px rgba(0,0,0,.04)}
.service-title{position:absolute;left:0;width:100%;text-align:center;color:var(--ink)}
.service-tag{position:absolute;left:0;width:100%;text-align:center;font-size:2.8px;color:#999;letter-spacing:.3px}
.service-copy{position:absolute;left:18px;right:18px;text-align:center;color:var(--muted)}
.preview-link{position:absolute;left:0;width:100%;text-align:center;color:var(--teal);font-weight:500}
.preview-link span{border-bottom:1px solid var(--teal);padding-bottom:.5px}
.divider{position:absolute;height:1px;background:#a9dcd7}

/* about coach */
.coach-card{position:absolute;background:var(--teal);border-radius:8px;overflow:visible}
.coach-halo{position:absolute;width:54px;height:54px;border-radius:50%;background:var(--teal)}
.coach-title{position:absolute;left:17px;font-size:11px;color:#fff;font-weight:400}
.coach-rule{position:absolute;left:17px;width:26px;height:1px;background:#bfe9e4}
.coach-sub{position:absolute;left:17px;font-size:4.6px;color:#e8f7f5}
.coach-copy{position:absolute;left:17px;width:184px;font-size:4.7px;line-height:9.5px;color:#eefaf8}
.btn-ghost{position:absolute;border:1px solid #d8f1ee;color:#fff;font-size:5.3px;display:flex;align-items:center;justify-content:center;border-radius:2px}

/* testimonials */
.section-title{position:absolute;left:0;width:100%;text-align:center;font-size:11px;font-weight:500}
.section-sub{position:absolute;left:0;width:100%;text-align:center;font-size:4.4px;color:var(--ink)}
.quote-back{position:absolute;border:1px solid #cfd8d8;background:#fff}
.quote-card{position:absolute;border:1px solid var(--teal);background:#fff}
.quote-text{position:absolute;left:9px;right:9px;text-align:center;font-size:4.7px;line-height:9.3px;color:var(--ink)}
.avatar{position:absolute;width:34px;height:34px;border-radius:50%;border:1.5px solid var(--teal);background:linear-gradient(160deg,#c9a58a,#8f6e5a)}
.arrow{position:absolute;width:22px;height:10px}

/* tiles */
.tile{position:absolute;height:77px;border-radius:2px;overflow:hidden;display:flex;align-items:center;justify-content:center}
.tile-label{position:relative;color:#fff;font-size:9.4px;font-weight:500}

.quote-big{position:absolute;left:0;width:100%;text-align:center;font-size:10.4px;line-height:15.5px;font-weight:400}
.quote-author{position:absolute;left:0;width:100%;text-align:center;font-size:2.9px;letter-spacing:.2px}

/* newsletter */
.newsletter{position:absolute;left:30px;top:642px;width:326px;height:161px;background:var(--panel);border-radius:6px}
.email-field{position:absolute;left:79px;top:742px;width:160px;height:20px;background:#fff;font-size:6px;color:#b9b9b9;display:flex;align-items:center;padding-left:6px}

/* cta + footer */
.cta{position:absolute;left:0;top:838px;width:100%;height:114px;background:var(--teal)}
.footer{position:absolute;left:0;top:953px;width:100%;height:68px;background:var(--teal)}
.foot-link{position:absolute;font-size:4.6px;color:#fff}
.social{position:absolute;width:10px;height:10px;border:.8px solid #fff;border-radius:50%}
</style>
</head>
<body>

<!-- Home page, upper part -->
<section class="page page-home">
  <header class="nav">
    <div class="brand"><span class="brand-ring"></span><span class="brand-name">RISING PATHS</span></div>
    <span class="nav-link" style="left:161px">Home</span>
    <span class="nav-link" style="left:196px">About</span>
    <span class="nav-link" style="left:229px">Services</span>
    <span class="nav-link" style="left:270px">Blogs</span>
    <span class="btn-outline-teal" style="left:308px;top:8px;width:52px;height:16px">Contact Now</span>
  </header>

  <div class="hero" role="img" aria-label="Warm photo of a woman in a knit sweater embracing someone">
    <div class="hero-shade"></div>
  </div>
  <h1 class="hero-title"><span class="accent">Rising</span> Paths Life Coaching</h1>
  <div class="hero-rule" style="top:106px"></div>
  <p class="hero-copy" style="top:120px">Lorem insum dolor amet consec tetur adiriscin elit eiusmod temsor incididunt dolore masna alirua enim minim.</p>
  <span class="btn-solid" style="left:125px;top:172px;width:70px;height:21px">Read More</span>
  <span class="btn-white" style="left:195px;top:172px;width:70px;height:21px">Biography</span>

  <!-- featured services -->
  <article class="service-card" style="left:31px;top:234px;width:161px;height:236px">
    <div class="photo" style="left:0;top:0;width:161px;height:93px;background:linear-gradient(135deg,#e9e6e0,#cfc8bd 60%,#8a8a6a)" role="img" aria-label="Cup of black coffee with lavender sprigs"></div>
    <h3 class="service-title" style="top:109px;font-size:10.6px;line-height:15.3px;font-weight:400">Ellum Dolorem Fusiat Boluntas Nulla Sariatur Exceur Sante</h3>
    <p class="service-tag" style="top:158px">SERVICES AREA</p>
    <p class="service-copy" style="top:173px;font-size:5px;line-height:10px">Furit masni dolores ratione nesciunt nerue ruisruam dolorem insum dolor amet consectetur excur sante.</p>
    <p class="preview-link" style="top:211px;font-size:5.6px"><span>PREVIEW MORE</span></p>
  </article>
  <article class="service-card" style="left:198px;top:234px;width:161px;height:236px">
    <div class="photo" style="left:0;top:0;width:161px;height:93px;background:linear-gradient(160deg,#c4ccd2,#a3977f 55%,#6a5a4c)" role="img" aria-label="Three laughing friends walking outdoors"></div>
    <h3 class="service-title" style="top:109px;font-size:10.6px;line-height:15.3px;font-weight:400">Ratione Ecseur Serue Isruam Dolor Himpla Unsum Sapiur</h3>
    <p class="service-tag" style="top:158px">SERVICES AREA</p>
    <p class="service-copy" style="top:175px;font-size:5px;line-height:10px">Furit masni dolores ratione nesciunt nerue ruisruam dolorem insum dolor amet consectetur excur sante.</p>
    <p class="preview-link" style="top:211px;font-size:5.6px"><span>PREVIEW MORE</span></p>
  </article>

  <article class="service-card" style="left:31px;top:475px;width:106px;height:159px">
    <div class="photo" style="left:0;top:0;width:106px;height:74px;background:linear-gradient(135deg,#f1eee9,#e4d6d0 60%,#c9b49a)" role="img" aria-label="Desk with laptop, lamp and pink flowers"></div>
    <h3 class="service-title" style="top:86px;font-size:9.4px;font-weight:400">Life Coaching</h3>
    <p class="service-copy" style="left:12px;right:12px;top:113px;font-size:4.6px;line-height:8px">Furit masni dolores ratione nesciunt nerue</p>
    <p class="preview-link" style="top:138px;font-size:4.4px"><span>PREVIEW MORE</span></p>
  </article>
  <article class="service-card" style="left:143px;top:475px;width:106px;height:159px">
    <div class="photo" style="left:0;top:0;width:106px;height:74px;background:linear-gradient(180deg,#c9cfd3,#8b8475 55%,#b59e74)" role="img" aria-label="Dark off-road vehicle in a dry field"></div>
    <h3 class="service-title" style="top:86px;font-size:9.4px;font-weight:400">Career Coaching</h3>
    <p class="service-copy" style="left:12px;right:12px;top:113px;font-size:4.6px;line-height:8px">Furit masni dolores ratione nesciunt nerue</p>
    <p class="preview-link" style="top:138px;font-size:4.4px"><span>PREVIEW MORE</span></p>
  </article>
  <article class="service-card" style="left:255px;top:475px;width:106px;height:159px">
    <div class="photo" style="left:0;top:0;width:106px;height:74px;background:linear-gradient(135deg,#e8e2dc,#b48f71 55%,#8d4a3a)" role="img" aria-label="Pancakes with berries and chocolate on a plate"></div>
    <h3 class="service-title" style="top:86px;font-size:9.4px;line-height:14px;font-weight:400">Relationship Coaching</h3>
    <p class="service-copy" style="left:12px;right:12px;top:113px;font-size:4.6px;line-height:8px">Furit masni dolores ratione nesciunt nerue</p>
    <p class="preview-link" style="top:138px;font-size:4.4px"><span>PREVIEW MORE</span></p>
  </article>

  <div class="divider" style="left:31px;top:659px;width:134px"></div>
  <div class="divider" style="left:224px;top:659px;width:136px"></div>
  <span class="btn-outline-teal" style="left:170px;top:652px;width:49px;height:15px;font-size:5.4px">All Services</span>

  <!-- about coach -->
  <div class="coach-halo" style="left:270px;top:710px"></div>
  <div class="coach-card" style="left:31px;top:731px;width:329px;height:161px">
    <h2 class="coach-title" style="top:25px">About Coach</h2>
    <div class="coach-rule" style="top:41px"></div>
    <p class="coach-sub" style="top:45px">Passionate Life Coach</p>
    <p class="coach-copy" style="top:64px">We have been working as Life Coaches since 2010. We specialize in helping people identify and achieve their personal goals by coping with the issues that are causing them distress, anxiety, and stress. We take great pride in the progress and success of our clients, and look forward to helping you.</p>
    <span class="btn-ghost" style="left:17px;top:120px;width:48px;height:16px">Learn More</span>
  </div>
  <div class="photo" style="left:240px;top:712px;width:116px;height:180px;background:linear-gradient(180deg,#f3f3f3,#e2e4e6 70%,#2a2a2a);border-radius:40px 40px 0 0" role="img" aria-label="Smiling coach in a white shirt with arms crossed"></div>

  <!-- testimonials -->
  <h2 class="section-title" style="top:928px">Testimonials</h2>
  <p class="section-sub" style="top:951px">It is a long established fact that a reader will be distracted by the readable</p>
  <div class="quote-back" style="left:79px;top:994px;width:231px;height:80px"></div>
  <div class="quote-card" style="left:99px;top:981px;width:191px;height:90px">
    <p class="quote-text" style="top:21px">It is a long established fact that a reader will be distracted by the readable content of a page when looking at its layout. The point of using Lorem Ipsum is that it has a more-or-less normal distribution of letters, as opposed to using 'Content here, content here' making it look like readable English.</p>
  </div>
  <div class="avatar" role="img" aria-label="Portrait of a client" style="left:178px;top:964px"></div>
  <svg class="arrow" style="left:38px;top:1017px" viewBox="0 0 22 10"><path d="M21 5H2M6 1L2 5l4 4" fill="none" stroke="#7a7a7a" stroke-width="1"/></svg>
  <svg class="arrow" style="left:333px;top:1017px" viewBox="0 0 22 10"><path d="M1 5h19M16 1l4 4-4 4" fill="none" stroke="#0aa497" stroke-width="1.2"/></svg>
</section>

<!-- Home page, lower part -->
<section class="page page-more">
  <div class="divider" style="left:0;top:0;width:387px"></div>
  <span class="btn-outline-teal" style="left:168px;top:-6px;width:48px;height:15px;font-size:5.4px">All Services</span>

  <div class="coach-halo" style="left:269px;top:52px"></div>
  <div class="coach-card" style="left:30px;top:74px;width:326px;height:160px">
    <h2 class="coach-title" style="top:25px">About Coach</h2>
    <div class="coach-rule" style="top:41px"></div>
    <p class="coach-sub" style="top:45px">Passionate Life Coach</p>
    <p class="coach-copy" style="top:64px">We have been working as Life Coaches since 2010. We specialize in helping people identify and achieve their personal goals by coping with the issues that are causing them distress, anxiety, and stress. We take great pride in the progress and success of our clients, and look forward to helping you.</p>
    <span class="btn-ghost" style="left:17px;top:119px;width:48px;height:16px">Learn More</span>
  </div>
  <div class="photo" style="left:238px;top:54px;width:116px;height:180px;background:linear-gradient(180deg,#f3f3f3,#e2e4e6 70%,#2a2a2a);border-radius:40px 40px 0 0" role="img" aria-label="Smiling coach in a white shirt with arms crossed"></div>

  <h2 class="section-title" style="top:268px">Testimonials</h2>
  <p class="section-sub" style="top:289px">It is a long established fact that a reader will be distracted by the readable</p>
  <div class="quote-back" style="left:79px;top:333px;width:228px;height:63px"></div>
  <div class="quote-card" style="left:98px;top:320px;width:189px;height:90px">
    <p class="quote-text" style="top:21px;font-size:4.6px;line-height:9.2px">It is a long established fact that a reader will be distracted by the readable content of a page when looking at its layout. The point of using Lorem Ipsum is that it has a more-or-less normal distribution of letters, as opposed to using 'Content here, content here' making it look like readable English.</p>
    <p class="abs center" style="left:0;width:100%;top:73px;font-size:5.5px;color:var(--teal);font-weight:500">Nora Pell</p>
    <p class="abs center" style="left:0;width:100%;top:81px;font-size:2.8px;color:var(--muted)">22 June 2022</p>
  </div>
  <div class="avatar" role="img" aria-label="Portrait of a client" style="left:176px;top:300px"></div>
  <svg class="arrow" style="left:37px;top:356px" viewBox="0 0 22 10"><path d="M21 5H2M6 1L2 5l4 4" fill="none" stroke="#7a7a7a" stroke-width="1"/></svg>
  <svg class="arrow" style="left:329px;top:356px" viewBox="0 0 22 10"><path d="M1 5h19M16 1l4 4-4 4" fill="none" stroke="#0aa497" stroke-width="1.2"/></svg>

  <div class="tile" style="left:30px;top:445px;width:106px;background:linear-gradient(135deg,#5b5a55,#3a3936)" role="img" aria-label="Man on a motorcycle"><span class="tile-label">My E-books</span></div>
  <div class="tile" style="left:141px;top:445px;width:105px;background:linear-gradient(135deg,#7a6558,#4b3c35)" role="img" aria-label="Tea cup with open book and flowers"><span class="tile-label">Story</span></div>
  <div class="tile" style="left:251px;top:445px;width:106px;background:linear-gradient(180deg,#8c949a,#4f5458)" role="img" aria-label="Seaside skate park with palm trees"><span class="tile-label">History</span></div>

  <p class="quote-big" style="top:547px">“Architecto beatae. Vitae dicta exslicabo<br>enim ipsam volus tatem volusta dolor.”</p>
  <p class="quote-author" style="top:581px">EVAN MARLOW</p>

  <div class="abs" style="left:193px;top:620px;width:1px;height:35px;background:#9fcfca"></div>
  <div class="newsletter"></div>
  <h2 class="section-title" style="top:683px">Join Our Daily Newsletter</h2>
  <p class="abs center" style="left:70px;width:247px;top:711px;font-size:5.6px;line-height:9px">Exercita tionem ullam cornoris suscihit labori commodi autem resreh enderit volustate morums.</p>
  <div class="email-field">Email</div>
  <span class="btn-solid" style="left:239px;top:742px;width:69px;height:20px">Subscribe</span>

  <div class="cta"></div>
  <div class="coach-halo" style="left:50px;top:820px;width:45px;height:45px"></div>
  <div class="photo" style="left:34px;top:828px;width:86px;height:124px;background:linear-gradient(180deg,#a1694c,#d84b4f 55%,#b63c40);border-radius:30px 30px 0 0" role="img" aria-label="Smiling woman in a red top holding a book"></div>
  <h2 class="abs" style="left:153px;top:858px;font-size:10.5px;font-weight:500;color:#fff">Make your life better!</h2>
  <p class="abs" style="left:153px;top:881px;width:206px;font-size:5.3px;line-height:9px;color:#eefaf8">Lorem insum dolor amet consec tetur adiriscin elit eiusmod temsor incididunt dolore masna alirua minim veniam nostrud exerci tation conseruat.</p>
  <span class="btn-ghost" style="left:153px;top:920px;width:48px;height:16px">Learn More</span>

  <div class="footer"></div>
  <div class="abs" style="left:0;top:952px;width:100%;height:1px;background:#66c9c0"></div>
  <p class="abs center" style="left:0;width:100%;top:965px;font-size:6.8px;color:#fff;padding-left:14px">Let's Talk?</p>
  <span class="foot-link" style="left:144px;top:984px">Services</span>
  <span class="foot-link" style="left:190px;top:984px">Contact</span>
  <span class="foot-link" style="left:234px;top:984px">Blogs</span>
  <div class="abs" style="left:48px;top:1000px;width:303px;height:1px;background:#66c9c0"></div>
  <span class="foot-link" style="left:48px;top:1006px;font-size:3.6px">2022 by Rising Paths Life Coaching</span>
  <span class="social" style="left:298px;top:1005px"></span>
  <span class="social" style="left:320px;top:1005px"></span>
  <span class="social" style="left:341px;top:1005px"></span>
</section>

</body>
</html>
```